Webdesign für Comic Shop
Zielgruppe
Webdesign: Jugendliche und junge Erwachsene zwischen 14 & 25 Jahren; Manga - Card Game - Comic und Anime Fans
Shop: Auch für Comic Händler & Großhändler ansprechend, einfach strukturiert aber trotzdem modern und eine fröhliche Farbgestaltung
Mobile Website: jugendlich
Flyer: für jugendliche
Aufgabenstellung
Designt werden sollen folgende Komponenten:
(1) webdesign für Comicshop mit 5 Filialen, gegliedert in "Home" und die Unterseiten der Filialen; Startseite plus eine Unterseite, Inhalte: Bilder unserer Filialen und unseres Teams, Events in unseren Shops, Vorstellung unseres Sortimentes, Blog was so los ist auf dem Comic Markt, Name HEFT HORIZONT, Newsletter, Plauderbuch - Zwitscha - RSS Button; Bilder von Events
(2) Mobile Website
Htlm5 website, die über Android oder iPhone Browser zu erreichen ist; Home: alle 5 Filialen als Button zum anklicken; Untermenüpunkt 1 - 1. Filiale - Untermenüpunkt 2 - 2. Filiale usw; in den einzelnen Filialen ein Button mit "Events" und "Kontakt" und "Bilder", unter dem Button "Kontakt" ein Button mit der Telefonnummer, die man direkt anwählen kann
(3) Shop
passend zum webdesign mit Händleranbindung, der Shop basiert auf der Grundlage von http://www.ladenkern.de/; das design soll sich eng am ladenkern-demo-shop orientieren; für die Artikellieferbarkeiten bitte das "Comicmännchen" unseres Logos verwenden mit verschiedenen Posen für "lieferbar" - "noch geringe Mengen lieferbar" - "ausverkauft" - "Neuheit" - "bald lieferbar";
(4) Logoumgestaltung
Ein Vorschlag liegt von uns vor, der professionel als LOGO gestaltet werden soll - Farbgestaltung: 4farbig, Photoshop Vektor Datei, grelles grün, kräftiges blau, schwarz, weiss

```html
<!DOCTYPE html>
<html lang="de">
<head>
<meta charset="utf-8">
<title>HEFT HORIZONT – Osnabrück</title>
<link href="https://fonts.googleapis.com/css2?family=Arimo:wght@400;700&display=swap" rel="stylesheet">
<style>
  :root {
    --space-deep: #060d22;
    --space-mid: #14386e;
    --space-low: #0a1630;
    --body-top: #1d2227;
    --body-bottom: #0c0f12;
    --brand-text: #e8f3ff;
    --city-bg: #f6f0c9;
    --city-border: #fdfbea;
    --city-text: #2f8a22;
    --btn-top: #6a737d;
    --btn-bottom: #3a4047;
    --btn-border: #8a939c;
    --btn-text: #e4ecf3;
    --mail-text: #a9d6f7;
    --footer-text: #cfd3d7;
  }
  * { box-sizing: border-box; margin: 0; padding: 0; }
  html, body { width: 927px; height: 1200px; overflow: hidden; }
  body {
    font-family: "Arimo", Arial, sans-serif;
    background: linear-gradient(180deg, var(--body-top) 0%, var(--body-bottom) 100%);
    position: relative;
  }
  .hero {
    position: absolute; left: 0; top: 0; width: 927px; height: 480px;
    background: linear-gradient(180deg, var(--space-deep) 0%, var(--space-mid) 60%, var(--space-low) 100%);
  }
  .brand-name {
    position: absolute; left: 0; top: 34px; width: 927px;
    text-align: center; font-weight: 700; font-size: 96px; letter-spacing: 6px;
    line-height: 110px; color: var(--brand-text);
  }
  .city {
    position: absolute; left: 34px; top: 511px; width: 860px; height: 141px;
    background: var(--city-bg); border: 5px solid var(--city-border); border-radius: 16px;
    display: flex; align-items: center; justify-content: center;
    font-weight: 700; font-size: 76px; color: var(--city-text);
  }
  .action {
    position: absolute; left: 34px; width: 860px; height: 86px;
    background: linear-gradient(180deg, var(--btn-top) 0%, var(--btn-bottom) 100%);
    border: 3px solid var(--btn-border); border-radius: 16px;
    display: flex; align-items: center; justify-content: center;
    font-weight: 700; font-size: 52px; color: var(--btn-text);
    text-decoration: none; white-space: nowrap;
  }
  .action-phone { top: 707px; }
  .action-mail { top: 836px; color: var(--mail-text); font-size: 50px; }
  .action-events { top: 969px; }
  .footer-links {
    position: absolute; left: 0; top: 1120px; width: 927px;
    text-align: center; font-size: 37px; color: var(--footer-text);
  }
  .footer-links a { color: inherit; text-decoration: none; }
</style>
</head>
<body>
  <header class="hero" role="img" aria-label="Weltraumszene mit Planet und Comic-Maskottchen"></header>
  <div class="brand-name">HEFT HORIZONT</div>

  <h1 class="city">OSNABRÜCK</h1>

  <a class="action action-phone" href="tel:05414817290">TEL: 0541 - 4817290</a>
  <a class="action action-mail" href="mailto:heft-horizont-os@postfach.de">heft-horizont-os@postfach.de</a>
  <a class="action action-events" href="#events">UNSERE EVENTS</a>

  <nav class="footer-links"><a href="#karte">Kartenblick</a> | <a href="#impressum">Impressum</a></nav>
</body>
</html>
```